Bold Website Design for Fitness Trainer - No Coding

We are in need of a bold and unique website design for a personal fitness training company, www.TessaLorvel.com. We need DESIGN ONLY for three pages. These will be a homepage, a lead capture page, and one internal page with a sidebar. The design will be used for coding a wordpress theme, if that matters for the designer.

Tessa Lorvel Fitness Training
2738 E 19th St #415
Austin, TX 78705
512-607-4918
http://www.tessalorvel.com

Target Market(s)

18-45 year old male and females making 80k+ a year and looking to get stronger and in shape.

Industry/Entity Type

Fitness

Number of Pages Required

3 page

Font styles to use
Sans Serif

Requirements
Must have
• See attached design specs file.
Nice to have
Should not have
• Boxed layout.
• Dark Background.

```html
<!DOCTYPE html>
<html lang="en">
<head>
<meta charset="utf-8">
<title>Tessa Lorvel Fitness Training</title>
<link href="https://fonts.googleapis.com/css2?family=Oswald:wght@400;500&family=Open+Sans:wght@400;600;700&display=swap" rel="stylesheet">
<style>
:root{
  --cyan:#00b7ef;
  --cyan-soft:#3ec6f2;
  --navy:#0b1a4a;
  --dark:#2b2b2b;
  --darker:#1b1b1b;
  --ink:#222;
  --muted:#555;
  --light:#ececec;
  --pink:#e91e7a;
  --yellow:#f5c400;
  --white:#fff;
}
*{box-sizing:border-box;margin:0;padding:0}
html,body{width:1200px;height:3093px;overflow:hidden}
body{font-family:"Open Sans",Arial,sans-serif;color:var(--ink);background:var(--white);position:relative}
.heading{font-family:"Oswald",Arial,sans-serif;font-weight:400;text-transform:uppercase}
section,header,footer,nav{position:absolute;left:0;width:1200px}

/* top bar */
.topbar{top:0;height:37px;background:var(--dark);color:#fff;font-size:17px;display:flex;align-items:center;justify-content:space-between;padding:0 132px}
.topbar span{display:flex;align-items:center;gap:10px}
.topbar .mail{font-size:14px}

/* brand */
.brand{top:37px;height:149px;background:radial-gradient(ellipse at center,#fff6e0 0%,#fff 60%);display:flex;align-items:center;justify-content:center;gap:16px}
.brand .dot{width:92px;height:92px;border-radius:50%;background:var(--yellow)}
.brand .name{font-family:"Oswald",Arial,sans-serif;font-weight:500;font-size:40px;color:var(--navy)}

/* nav */
.mainnav{top:186px;height:45px;background:var(--cyan);display:flex;padding-left:132px}
.mainnav a{color:#fff;text-decoration:none;font-size:15px;text-transform:uppercase;display:flex;align-items:center;justify-content:center;height:45px}
.mainnav a.active{background:var(--navy)}

/* hero */
.hero{top:231px;height:542px;background:linear-gradient(100deg,#3a3a3a 0%,#6b6b6b 35%,#9a9a9a 60%,#d9d9d9 100%)}
.hero .copy{position:absolute;right:148px;top:190px;text-align:right;color:#fff;font-size:34px;line-height:1.2;text-shadow:0 1px 3px rgba(0,0,0,.4)}
.hero .btn-outline{display:inline-block;margin-top:14px;border:2px solid #fff;width:234px;height:46px;line-height:42px;text-align:center;font-size:26px}
.arrow-circle{position:absolute;width:40px;height:40px;border:2px solid #fff;border-radius:50%}

/* titles */
.section-title{text-align:center;font-size:36px;color:var(--ink)}
.section-title em{font-style:normal;color:var(--cyan)}
.divider{width:520px;height:2px;margin:10px auto 0;position:relative;background:linear-gradient(90deg,transparent,#ccc 20%,#ccc 80%,transparent)}
.divider.light{background:linear-gradient(90deg,transparent,rgba(255,255,255,.8) 20%,rgba(255,255,255,.8) 80%,transparent)}
.divider i{position:absolute;top:-6px;width:12px;height:12px;border:2px solid #ccc;border-radius:50%;background:#fff}
.divider.light i{border-color:#fff;background:var(--cyan)}

/* about */
.about{top:773px;height:307px;padding-top:38px}
.about p{width:896px;margin:26px auto 0;text-align:center;font-size:13.4px;line-height:22px;color:var(--muted)}
.btn{display:block;margin:20px auto 0;width:148px;height:42px;line-height:42px;text-align:center;background:var(--cyan);color:#fff;font-family:"Oswald",Arial,sans-serif;font-size:17px}

/* services */
.services{top:1080px;height:388px;background:linear-gradient(180deg,#2fb8ea,#12b4ea)}
.services .section-title{color:#fff;margin-top:24px}
.service{position:absolute;top:112px;width:240px;text-align:center;color:#fff}
.service .ring{width:120px;height:120px;margin:0 auto;border-radius:50%;border:4px solid #fff;background:var(--white);display:flex;align-items:center;justify-content:center;box-shadow:inset 0 0 0 6px var(--cyan-soft)}
.service h3{font-family:"Oswald",Arial,sans-serif;font-weight:400;font-size:21px;margin-top:16px}
.service p{font-size:12.5px;line-height:19px;margin-top:4px}

/* testimonials */
.testimonials{top:1468px;height:287px;background:linear-gradient(180deg,#fafafa,#e4e4e4);padding-top:26px}
.testimonials .avatar{position:absolute;left:137px;top:116px;width:110px;height:110px;border-radius:50%;border:5px solid #fff;background:linear-gradient(#a7a0a6,#6a5d73);box-shadow:0 0 0 1px #ccc}
.testimonials blockquote{position:absolute;left:268px;top:118px;width:800px;font-style:italic;font-size:13px;line-height:24px;color:var(--muted)}
.testimonials blockquote b{font-size:46px;color:#bbb;font-family:Georgia,serif;vertical-align:-16px;margin-right:4px}
.testimonials cite{display:block;font-size:11.5px;color:#444;font-style:italic}
.chev{position:absolute;top:96px}

/* community */
.community{top:1755px;height:406px;background:linear-gradient(180deg,#3fc4ef,#29b5e6)}
.community .section-title{color:#fff;margin-top:20px}
.member{position:absolute;width:300px;display:flex;gap:14px;color:#fff}
.member .photo{flex:0 0 103px;height:103px;border:4px solid #fff;background:linear-gradient(#d6a98a,#8a5f4a)}
.member div p{font-size:11.5px;line-height:19px}
.member div p strong{font-weight:700}

/* blog */
.blog{top:2161px;height:427px;background:#ebebeb;padding-top:26px}
.post{position:absolute;width:293px}
.post .thumb{height:177px;background:linear-gradient(135deg,#6a6a6a,#b7a9a0);outline:1px solid #fff;outline-offset:-12px}
.post h4{font-size:15px;font-weight:400;margin-top:12px;color:var(--ink)}
.post p{font-size:12.5px;color:var(--muted);line-height:19px;margin-top:4px}
.post .meta{display:flex;gap:14px;align-items:center;margin-top:12px}
.bubble{width:38px;height:38px;border-radius:50%;background:#fff;display:flex;align-items:center;justify-content:center;font-size:11px;line-height:12px;text-align:center}
.date-badge{position:absolute;left:30px;top:26px;width:62px;height:62px;border-radius:50%;background:var(--pink);color:#fff;text-align:center;font-size:20px;line-height:22px;padding-top:8px;font-weight:600}
.date-badge small{display:block;font-size:13px}

/* cta */
.cta{top:2588px;height:196px;background:linear-gradient(180deg,#4ccbf2,#5fd1ea);text-align:center;padding-top:52px}
.cta h2{color:#fff;font-size:36px}
.cta .btn-yellow{display:inline-block;margin-top:20px;width:234px;height:46px;line-height:46px;background:var(--yellow);color:#222;font-family:"Oswald",Arial,sans-serif;font-size:22px}

/* footer */
.site-footer{top:2784px;height:260px;background:var(--dark);color:#fff;display:flex;padding:0 60px}
.col{flex:1;padding:26px 70px 0;font-size:13px}
.col + .col{border-left:1px solid #444}
.col h5{font-weight:400;font-size:18px;padding-bottom:10px;border-bottom:1px solid #555;margin-bottom:16px}
.col li{list-style:none;line-height:36px;display:flex;align-items:center;gap:12px}
.col .dot{width:14px;height:14px;border-radius:50%;background:#fff;display:inline-block}
.col.contact{text-align:center;padding:26px 40px 0}
.col.contact h5{margin:0 50px 16px}
.col.contact li{justify-content:center;align-items:flex-start;line-height:20px;margin-bottom:16px;white-space:nowrap}
.col.contact li svg{margin-top:3px;flex:0 0 auto}
.col.links{text-align:right}
.col.links li{justify-content:flex-end;line-height:25px}
.copyright{position:absolute;top:3044px;left:0;width:1200px;height:49px;background:var(--darker);color:#fff;font-size:13px;text-align:center;line-height:49px;font-weight:600}
</style>
</head>
<body>

<div class="topbar">
  <span><svg width="20" height="20" viewBox="0 0 20 20"><circle cx="10" cy="10" r="9" fill="none" stroke="#fff" stroke-width="1.6"/><path d="M7 5l2 2-1 1.5c.6 1.3 1.6 2.3 2.8 2.8L12 10l2 2-1.3 1.6C9.5 13.2 6.8 10.4 6 7.3z" fill="#fff"/></svg>512 607 4918</span>
  <span class="mail"><svg width="16" height="12" viewBox="0 0 16 12"><rect width="16" height="12" fill="#fff"/><path d="M0 0l8 6 8-6" fill="none" stroke="#2b2b2b" stroke-width="1.4"/></svg>info@tessalorvel.com</span>
</div>

<header class="brand">
  <span class="dot"></span>
  <span class="name">Tessa Lorvel</span>
</header>

<nav class="mainnav">
  <a class="active" href="#" style="width:132px">Home</a>
  <a href="#" style="width:130px">Programs</a>
  <a href="#" style="width:200px">Meet Your Trainer</a>
  <a href="#" style="width:100px">Blog</a>
  <a href="#" style="width:150px">Free Session</a>
  <a href="#" style="width:150px">Contact Us</a>
</nav>

<section class="hero" role="img" aria-label="Trainer spotting a woman lifting dumbbells on a bench in a gym">
  <span class="arrow-circle" style="left:93px;top:238px"></span>
  <span class="arrow-circle" style="left:1067px;top:238px"></span>
  <div class="copy heading">
    Get Started Today<br>Your First Sessions Is Free!<br>
    <span class="btn-outline">Sign Up Today</span>
  </div>
</section>

<section class="about">
  <h2 class="section-title heading">About <em>Tessa Lorvel</em></h2>
  <div class="divider" style="width:360px"></div>
  <p>Lorem ipsum dolor sit amet, consectetuer adipiscing elit, sed diam nonummy nibh euismod tincidunt ut laoreet dolore magna aliquam erat volutpat. Ut wisi enim ad minim veniam, quis nostrud exerci tation ullamcorper suscipit lobortis nisl ut aliquip ex ea commodo magna aliquam erat volutpat. Ut wisi enim ad minim veniam, quis nostrud exerci tation ullamcorper suscipit lobortis nisl ut aliquip ex ea commodo consequat. Duis autem vel eum iriure dolor in hendrerit in vulputate velit esse molestie</p>
  <span class="btn">READ MORE</span>
</section>

<section class="services" aria-label="Our services">
  <h2 class="section-title heading">Our Services</h2>
  <div class="divider light"><i style="left:248px"></i></div>
  <div class="service" style="left:127px"><div class="ring"><svg width="56" height="56" viewBox="0 0 56 56"><rect x="8" y="24" width="40" height="8" fill="var(--navy)"/><rect x="4" y="16" width="8" height="24" fill="var(--navy)"/><rect x="44" y="16" width="8" height="24" fill="var(--navy)"/></svg></div><h3>GENERAL FITNESS</h3><p>Lorem ipsum dolor sit amet,<br>consectetuer adipiscing elit,<br>nonummy nibh</p></div>
  <div class="service" style="left:375px"><div class="ring"><svg width="56" height="56" viewBox="0 0 56 56"><circle cx="28" cy="28" r="18" fill="none" stroke="var(--navy)" stroke-width="6"/><rect x="25" y="14" width="6" height="16" fill="var(--navy)"/></svg></div><h3>WEIGHT LOSS</h3><p>Lorem ipsum dolor sit amet,<br>consectetuer adipiscing elit,<br>nonummy nibh</p></div>
  <div class="service" style="left:614px"><div class="ring"><svg width="56" height="56" viewBox="0 0 56 56"><rect x="4" y="12" width="48" height="5" fill="var(--navy)"/><rect x="2" y="6" width="8" height="17" fill="var(--navy)"/><rect x="46" y="6" width="8" height="17" fill="var(--navy)"/><rect x="24" y="22" width="8" height="28" fill="var(--navy)"/></svg></div><h3>STRENGTH TRAINING</h3><p>Lorem ipsum dolor sit amet,<br>consectetuer adipiscing elit,<br>nonummy nibh</p></div>
  <div class="service" style="left:845px"><div class="ring"><svg width="56" height="56" viewBox="0 0 56 56"><rect x="6" y="40" width="44" height="6" fill="var(--navy)"/><rect x="4" y="30" width="10" height="20" fill="var(--navy)"/><rect x="42" y="30" width="10" height="20" fill="var(--navy)"/><path d="M18 36l10-26 10 26z" fill="var(--navy)"/></svg></div><h3>POWERLIFTING</h3><p>Lorem ipsum dolor sit amet,<br>consectetuer adipiscing elit,<br>nonummy nibh</p></div>
</section>

<section class="testimonials" aria-label="Client testimonials">
  <h2 class="section-title heading">Client Testimonials</h2>
  <div class="divider"></div>
  <svg class="chev" style="left:72px" width="24" height="24" viewBox="0 0 24 24"><path d="M15 4l-8 8 8 8" fill="none" stroke="#111" stroke-width="3.5"/></svg>
  <svg class="chev" style="left:1102px" width="24" height="24" viewBox="0 0 24 24"><path d="M9 4l8 8-8 8" fill="none" stroke="#111" stroke-width="3.5"/></svg>
  <div class="avatar" role="img" aria-label="Portrait of a client"></div>
  <blockquote><b>“</b>Lorem ipsum dolor sit amet, consectetuer adipiscing elit, sed diam nonummy nibh euismod tincidunt ut laoreet dolore magna aliquam erat volutpat. Ut wisi enim ad minim veniam, quis nostrud exerci tation ullamcorper suscipit lobortis nisl ut aliquip commodo consequat. Duis autem vel odio dignissimaugue duis dolore te feugait nulla facilisi.
    <cite>.... Marla Quen, Brightwell , USA</cite></blockquote>
</section>

<section class="community" aria-label="What our community is saying">
  <h2 class="section-title heading">What Our Community Is Saying</h2>
  <div class="divider light"><i style="left:248px"></i></div>
  <div class="member" style="left:134px;top:108px"><span class="photo" role="img" aria-label="Photo of a community member"></span><div><p><strong>Lorem ipsum dolor sit amet,</strong><br>Lorem ipsum dolor sit amet,<br>consectetuer adipiscing elit,<br>nonummy nibh<br><strong>Read More »</strong></p></div></div>
  <div class="member" style="left:462px;top:108px"><span class="photo" role="img" aria-label="Photo of a community member"></span><div><p><strong>Lorem ipsum dolor sit amet,</strong><br>Lorem ipsum dolor sit amet,<br>consectetuer adipiscing elit,<br>nonummy nibh<br><strong>Read More »</strong></p></div></div>
  <div class="member" style="left:784px;top:108px"><span class="photo" role="img" aria-label="Photo of a community member"></span><div><p><strong>Lorem ipsum dolor sit amet,</strong><br>Lorem ipsum dolor sit amet,<br>consectetuer adipiscing elit,<br>nonummy nibh<br><strong>Read More »</strong></p></div></div>
  <div class="member" style="left:134px;top:250px"><span class="photo" role="img" aria-label="Photo of a community member"></span><div><p><strong>Lorem ipsum dolor sit amet,</strong><br>Lorem ipsum dolor sit amet,<br>consectetuer adipiscing elit,<br>nonummy nibh<br><strong>Read More »</strong></p></div></div>
  <div class="member" style="left:462px;top:250px"><span class="photo" role="img" aria-label="Photo of a community member"></span><div><p><strong>Lorem ipsum dolor sit amet,</strong><br>Lorem ipsum dolor sit amet,<br>consectetuer adipiscing elit,<br>nonummy nibh<br><strong>Read More »</strong></p></div></div>
  <div class="member" style="left:784px;top:250px"><span class="photo" role="img" aria-label="Photo of a community member"></span><div><p><strong>Lorem ipsum dolor sit amet,</strong><br>Lorem ipsum dolor sit amet,<br>consectetuer adipiscing elit,<br>nonummy nibh<br><strong>Read More »</strong></p></div></div>
</section>

<section class="blog" aria-label="Latest blog">
  <h2 class="section-title heading">Latest Blog</h2>
  <div class="divider" style="width:320px"></div>
  <svg class="chev" style="left:86px;top:180px;position:absolute" width="30" height="54" viewBox="0 0 30 54"><path d="M26 2L4 27l22 25" fill="none" stroke="#111" stroke-width="2.5"/></svg>
  <svg class="chev" style="left:1082px;top:180px;position:absolute" width="30" height="54" viewBox="0 0 30 54"><path d="M4 2l22 25L4 52" fill="none" stroke="#111" stroke-width="2.5"/></svg>
  <article class="post" style="left:132px;top:95px">
    <div class="thumb" style="height:194px" role="img" aria-label="Trainer coaching a client with a dumbbell"></div>
    <span class="date-badge">12<small>JUNE</small></span>
    <h4 style="font-size:16px;margin-top:14px">LOREM IPSUM DOLOR SIT AMET</h4>
  </article>
  <article class="post" style="left:464px;top:95px">
    <div class="thumb" role="img" aria-label="Group stretching class in a studio"></div>
    <h4>Lorem Ipsum Dolor Sit Amet</h4>
    <p>Lorem ipsum dolor sit amet, consectetuer cing elit, sed diam nonummy nibh ismod tincidunt</p>
    <div class="meta"><span class="bubble" style="color:var(--pink)">♥</span><span class="bubble">●</span><span class="bubble">06<br>June</span></div>
  </article>
  <article class="post" style="left:790px;top:95px">
    <div class="thumb" role="img" aria-label="Trainer assisting a client at a gym machine"></div>
    <h4>Lorem Ipsum Dolor Sit Amet</h4>
    <p>Lorem ipsum dolor sit amet, consectetuer cing elit, sed diam nonummy nibh ismod tincidunt</p>
    <div class="meta"><span class="bubble" style="color:var(--pink)">♥</span><span class="bubble">●</span><span class="bubble">06<br>June</span></div>
  </article>
</section>

<section class="cta">
  <h2 class="heading">Get Started Today - Your First Sessions Is Free!</h2>
  <span class="btn-yellow">SIGN UP TODAY</span>
</section>

<footer class="site-footer">
  <div class="col">
    <h5>Connect With Us</h5>
    <ul><li><span class="dot"></span>Pagevale</li><li><span class="dot"></span>Chirpline</li><li><span class="dot"></span>Pinvale</li><li><span class="dot"></span>Clipvale</li></ul>
  </div>
  <div class="col contact">
    <h5>Contact Information</h5>
    <ul>
      <li><svg width="12" height="16" viewBox="0 0 12 16"><path d="M6 0a6 6 0 0 0-6 6c0 4 6 10 6 10s6-6 6-10a6 6 0 0 0-6-6z" fill="#fff"/><circle cx="6" cy="6" r="2" fill="#2b2b2b"/></svg><span>Lorem ipsum dolor consectetuer<br>bitasa street:395001</span></li>
      <li><svg width="14" height="14" viewBox="0 0 20 20"><path d="M4 1l4 4-2 3c1.3 2.6 3.3 4.6 6 6l3-2 4 4-3 3C8 18 2 12 1 4z" fill="#fff"/></svg>+12 123456789</li>
      <li><svg width="14" height="10" viewBox="0 0 16 12"><rect width="16" height="12" fill="#fff"/><path d="M0 0l8 6 8-6" fill="none" stroke="#2b2b2b" stroke-width="1.4"/></svg>info@yoursitename.com</li>
    </ul>
  </div>
  <div class="col links">
    <h5>Quick Links</h5>
    <ul><li>Home ‹</li><li>Programs ‹</li><li>Meet Your Trainer ‹</li><li>Blog ‹</li><li>Free Session ‹</li><li>Contact Us ‹</li></ul>
  </div>
</footer>
<div class="copyright">2015 Tessalorvel. All rights Reserved</div>

</body>
</html>
```